Dorian's Roam Almanac Mobile App

We need a sleek new design for our new mobile app we are launching in the South Pacific. This app will be released for both iPhone and Android. The app has already been developed and your new design will give it the finishing touch we need to release it to our audience. This will be the premiere tourism app for the South Pacific and will be advertised heavily in our successful print publications which are distributed internationally. We are looking for you to provide two designs (for two screens in our mobile app) for this competition. The selected winner will have the opportunity to design the remaining screens in our app and website as a separate contract.

Attached you will see a few of the screens that currently exist in our mobile app to give you a feel for the functionality. The two screens we want you to design for this competition are the main listing page and the category selection page. These two screens will be included in the uploaded files and will be clearly marked so you know what we are looking for.

Please feel free to reach out to us with any questions if you need any guidance in directing your designs. Show us something sleek, engaging, and ultimately something that will drive our users to want to engage with the businesses that are listed in the app.

Please see the uploaded files for a couple of our current designs, the two screens we want you to design for this competition, and a few samples of design ideas we like.

Best of Luck!

Target Market(s)

Travelers to the South Pacific

Industry/Entity Type

Travel Industry

Font styles to use
Serif
Sans Serif

Colors
0492cd
33a6d7
ec1f27
f04a50
85cae6
cee9f5
f59296
cedeed
fbd4d5

Requirements
Must have
• Clean, attractive design for the two screens mentioned in the brief.
Nice to have
• Icon sets, color guide, font selection
Should not have
• Project should not be too busy or incorporate too many different colors, styles, fonts, etc.

```html
<!DOCTYPE html>
<html lang="en">
<head>
<meta charset="utf-8">
<title>Dorian's Roam Almanac – Listing Screen</title>
<link rel="stylesheet" href="https://fonts.googleapis.com/css2?family=Inter:wght@400;500;600;700;800&display=swap">
<style>
  :root {
    --stage: #e9edf1;
    --screen: #ffffff;
    --ink: #1f1f1f;
    --muted: #8a8a8a;
    --line: #e4e4e4;
    --star: #f5a623;
    --pin-red: #ec1f27;
    --tag: #2b2b2b;
    --sky: #85cae6;
    --sea: #33a6d7;
    --deck: #8a6a4a;
    --map-base: #ecebe8;
    --map-road: #f8f8f6;
  }
  * { box-sizing: border-box; margin: 0; padding: 0; }
  html, body { width: 1200px; height: 1200px; overflow: hidden; }
  body {
    background: var(--stage);
    font-family: "Inter", "Helvetica Neue", Arial, sans-serif;
    color: var(--ink);
    position: relative;
  }
  .app-screen {
    position: absolute;
    left: 300px; top: 66px;
    width: 600px; height: 1067px;
    background: var(--screen);
    overflow: hidden;
    box-shadow: 0 20px 60px rgba(0,0,0,.12);
  }
  .hero-photo {
    position: absolute; left: 0; top: 0; width: 600px; height: 320px;
    background: linear-gradient(180deg, var(--sky) 0%, #cfe8f2 30%, var(--sea) 44%, #b9a184 58%, var(--deck) 100%);
  }
  .status-bar {
    position: absolute; left: 0; top: 0; width: 100%; height: 32px;
    display: flex; align-items: center; justify-content: space-between;
    padding: 0 14px; color: #fff; font-size: 18px; font-weight: 500;
  }
  .status-bar .carrier { display: flex; align-items: center; gap: 6px; }
  .status-bar .time { font-weight: 600; }
  .status-bar .battery { display: flex; align-items: center; gap: 6px; }
  .back-button { position: absolute; left: 22px; top: 72px; }
  .page-dots {
    position: absolute; left: 50%; top: 282px; transform: translateX(-50%);
    display: flex; gap: 8px; padding: 6px 12px; border-radius: 14px;
    background: rgba(255,255,255,.55);
  }
  .page-dots span { width: 9px; height: 9px; border-radius: 50%; background: rgba(255,255,255,.9); }
  .page-dots span.active { background: #3a3a3a; }

  .listing-title {
    position: absolute; left: 34px; top: 352px;
    font-size: 40px; font-weight: 800; letter-spacing: -0.5px;
  }
  .rating { position: absolute; left: 34px; top: 412px; display: flex; align-items: center; gap: 12px; }
  .rating .score { font-size: 34px; font-weight: 500; color: var(--muted); }
  .rating .stars { display: flex; gap: 2px; }
  .rating .reviews { font-size: 13px; color: var(--muted); margin-top: 4px; }

  .actions {
    position: absolute; left: 0; top: 480px; width: 600px; height: 118px;
    border-top: 1px solid var(--line); border-bottom: 1px solid var(--line);
    display: grid; grid-template-columns: repeat(3, 1fr);
  }
  .action {
    display: flex; flex-direction: column; align-items: center; justify-content: center; gap: 14px;
    font-size: 16px; color: #666; position: relative;
  }
  .action + .action::before {
    content: ""; position: absolute; left: 0; top: 34px; height: 50px; width: 1px; background: var(--line);
  }

  .location { position: absolute; left: 0; top: 598px; width: 600px; height: 200px; border-bottom: 1px solid var(--line); }
  .location .map {
    position: absolute; right: 0; top: 0; width: 330px; height: 200px;
    background: linear-gradient(90deg, rgba(236,235,232,0) 0%, var(--map-base) 40%, #e3e1dc 100%);
  }
  .location .address { position: absolute; left: 34px; top: 44px; display: flex; gap: 16px; }
  .location .address p { font-size: 19px; line-height: 1.35; font-weight: 500; }
  .location .tag {
    position: absolute; left: 78px; top: 130px;
    background: var(--tag); color: #fff; font-size: 14px; font-weight: 500;
    padding: 8px 12px; border-radius: 3px;
  }

  .directions {
    position: absolute; left: 0; top: 798px; width: 600px; height: 88px;
    border-bottom: 1px solid var(--line);
    display: flex; align-items: center; justify-content: center; gap: 12px;
    font-size: 18px; color: #444; padding-left: 180px;
  }
  .section-heading { position: absolute; left: 34px; top: 918px; font-size: 22px; font-weight: 700; }
</style>
</head>
<body>
  <main class="app-screen">
    <div class="hero-photo" role="img" aria-label="Photo of the resort's wooden sun deck with loungers, palm trees and the sea under a blue sky"></div>

    <div class="status-bar">
      <span class="carrier">●●●●● Roam
        <svg width="18" height="14" viewBox="0 0 18 14"><path d="M1 5a12 12 0 0 1 16 0M4 8a7.5 7.5 0 0 1 10 0M7 11a3 3 0 0 1 4 0" fill="none" stroke="#fff" stroke-width="2" stroke-linecap="round"/></svg>
      </span>
      <span class="time">9:41 AM</span>
      <span class="battery">100%
        <svg width="30" height="14" viewBox="0 0 30 14"><rect x="1" y="1" width="25" height="12" rx="2" fill="none" stroke="#fff" stroke-width="1.5"/><rect x="3" y="3" width="21" height="8" fill="#fff"/><rect x="27" y="4.5" width="2" height="5" fill="#fff"/></svg>
      </span>
    </div>

    <svg class="back-button" width="34" height="28" viewBox="0 0 34 28" aria-label="Back"><path d="M32 14H4M14 3 3 14l11 11" fill="none" stroke="#fff" stroke-width="3" stroke-linecap="round" stroke-linejoin="round"/></svg>

    <div class="page-dots"><span class="active"></span><span></span><span></span><span></span></div>

    <h1 class="listing-title">Lagoon Reef Lodge</h1>

    <div class="rating">
      <span class="score">4.5</span>
      <div>
        <div class="stars">
          <svg width="110" height="20" viewBox="0 0 110 20">
            <defs>
              <path id="star" d="M10 1l2.7 5.6 6.1.8-4.4 4.3 1 6.1L10 15l-5.4 2.8 1-6.1L1.2 7.4l6.1-.8z"/>
              <linearGradient id="half"><stop offset="50%" stop-color="#f5a623"/><stop offset="50%" stop-color="#fff"/></linearGradient>
            </defs>
            <use href="#star" fill="#f5a623"/>
            <use href="#star" x="22" fill="#f5a623"/>
            <use href="#star" x="44" fill="#f5a623"/>
            <use href="#star" x="66" fill="#f5a623"/>
            <use href="#star" x="88" fill="url(#half)" stroke="#f5a623" stroke-width="1"/>
          </svg>
        </div>
        <div class="reviews">2.3K Reviews</div>
      </div>
    </div>

    <section class="actions">
      <div class="action">
        <span>Add to Itinerary</span>
        <svg width="36" height="30" viewBox="0 0 36 30"><circle cx="6" cy="6" r="4" fill="none" stroke="#222" stroke-width="2.5"/><path d="M10 6h14a5 5 0 0 1 0 10H10a5 5 0 0 0 0 10h12" fill="none" stroke="#222" stroke-width="2.5" stroke-linecap="round"/><path d="M30 21v8M26 25h8" stroke="#222" stroke-width="2.5" stroke-linecap="round"/></svg>
      </div>
      <div class="action">
        <span>Check in</span>
        <svg width="26" height="32" viewBox="0 0 26 32"><path d="M13 30s11-11 11-18A11 11 0 0 0 2 12c0 7 11 18 11 18z" fill="none" stroke="#222" stroke-width="2.5"/><path d="M13 7v10M8 12h10" stroke="#222" stroke-width="2.5" stroke-linecap="round"/></svg>
      </div>
      <div class="action">
        <span>Add to Favorites</span>
        <svg width="32" height="28" viewBox="0 0 32 28"><path d="M16 26S2 17 2 9a7 7 0 0 1 14-2 7 7 0 0 1 14 2c0 8-14 17-14 17z" fill="none" stroke="#222" stroke-width="2.5" stroke-linejoin="round"/></svg>
      </div>
    </section>

    <section class="location">
      <div class="map" role="img" aria-label="Street map around the lodge with a red location marker"></div>
      <div class="address">
        <svg width="18" height="24" viewBox="0 0 18 24"><path d="M9 23s8-8 8-14A8 8 0 0 0 1 9c0 6 8 14 8 14z" fill="var(--pin-red)"/><circle cx="9" cy="9" r="3" fill="#fff"/></svg>
        <p>Palm Road, Ngatangiia, 48<br>Coral Isle, South Pacific</p>
      </div>
      <span class="tag">2+ Locations</span>
    </section>

    <div class="directions">
      <svg width="24" height="24" viewBox="0 0 24 24"><circle cx="12" cy="12" r="10" fill="none" stroke="#666" stroke-width="2"/><path d="M16 8l-2.5 5.5L8 16l2.5-5.5z" fill="none" stroke="#666" stroke-width="1.8" stroke-linejoin="round"/></svg>
      <span>Directions</span>
    </div>

    <h2 class="section-heading">Description</h2>
  </main>
</body>
</html>
```